Home care agency

Current website QRVCAREPLUS.com. Need to update and reformat to different pages. use my info from my current website

Target Market(s)

adult children

Industry/Entity Type

Home Health

Coding

Coded - Design and coding required

Number of Pages Required

4 page

Font styles to use
Sans Serif

Colors
3276b5
33a6d7
3277b5
85cae6
85acd3

```html
<!DOCTYPE html>
<html lang="en">
<head>
<meta charset="utf-8">
<title>Hearthside Home Health Services</title>
<link rel="stylesheet" href="https://fonts.googleapis.com/css2?family=Roboto+Slab:wght@400;700&family=Open+Sans:wght@400;600;700&family=Dancing+Script:wght@500&display=swap">
<style>
:root{
  --blue:#3276b5;
  --blue-dark:#2a649d;
  --teal:#2fb0ad;
  --teal-dark:#23918f;
  --sky:#85cae6;
  --mist:#85acd3;
  --ink:#2c3e50;
  --text:#6b7680;
  --line:#e3e8ec;
  --white:#ffffff;
  --navy:#21476b;
}
*{box-sizing:border-box;margin:0;padding:0}
html,body{width:1200px;height:3732px;overflow:hidden;background:var(--white)}
body{font-family:"Open Sans",Arial,sans-serif;color:var(--text);position:relative}
.slab{font-family:"Roboto Slab",Georgia,serif}
.script{font-family:"Dancing Script",cursive}

/* header */
.site-header{position:absolute;top:0;left:0;width:1200px;height:120px;background:var(--white)}
.brand{position:absolute;left:40px;top:8px;display:flex;align-items:center;gap:12px}
.brand-dot{width:110px;height:110px;border-radius:50%;border:3px solid var(--sky);display:flex;align-items:center;justify-content:center;background:var(--white)}
.brand-name{font-family:"Open Sans",sans-serif;font-weight:600;font-size:13px;color:var(--blue);text-align:center;line-height:1.3}
.header-phone{position:absolute;right:40px;top:12px;display:flex;align-items:center;gap:10px}
.header-phone .ico{width:36px;height:36px;border-radius:50%;background:var(--blue);display:flex;align-items:center;justify-content:center}
.header-phone small{display:block;font-size:11px;color:var(--text)}
.header-phone strong{font-size:22px;color:var(--blue)}
.main-nav{position:absolute;left:230px;top:72px;width:970px;height:44px;background:var(--teal);display:flex;align-items:center}
.main-nav a{color:var(--white);text-decoration:none;font-size:14px;font-weight:600;text-transform:uppercase;padding:0 30px;height:44px;line-height:44px}
.main-nav a.active{background:var(--blue)}

/* hero */
.hero{position:absolute;top:120px;left:0;width:1200px;height:512px;background:linear-gradient(110deg,#c9dbe6 0%,#e8eef1 45%,#b8a59a 75%,#8f7b70 100%)}
.hero::after{content:"";position:absolute;left:0;bottom:0;width:100%;height:140px;background:linear-gradient(0deg,rgba(47,176,173,.85),rgba(47,176,173,0))}
.hero-copy{position:absolute;left:80px;top:278px;z-index:2;color:var(--white)}
.hero-copy .kicker{font-size:30px;font-weight:400}
.hero-copy h1{font-size:66px;font-weight:700;letter-spacing:1px;line-height:1.05}
.hero-copy .sub{font-size:26px;letter-spacing:2px;margin-top:2px}
.btn{display:inline-block;background:var(--blue);color:var(--white);font-family:"Roboto Slab",serif;font-weight:700;font-size:17px;padding:14px 28px;text-transform:uppercase;letter-spacing:1px}
.hero-copy .btn{margin-top:26px}
.hero-dots{position:absolute;right:34px;top:210px;z-index:2;display:flex;flex-direction:column;gap:12px}
.hero-dots span{width:16px;height:16px;border-radius:50%;border:2px solid var(--white)}
.hero-dots span.on{background:var(--blue-dark);border-color:var(--white)}

/* about */
.about{position:absolute;top:632px;left:0;width:1200px;height:388px;background:var(--teal)}
.about-badge{position:absolute;left:150px;top:58px;width:280px;height:280px;border-radius:50%;border:4px dashed var(--sky);display:flex;flex-direction:column;align-items:center;justify-content:center;color:var(--white)}
.about-badge h2{font-size:42px;font-weight:700;letter-spacing:2px}
.about-badge p{font-size:22px}
.about-text{position:absolute;left:490px;top:50px;width:640px;color:var(--white);font-size:15px;line-height:1.75}
.about-text p+p{margin-top:16px}
.about-text .more{display:inline-block;margin-top:18px;font-family:"Roboto Slab",serif;font-weight:700;font-size:17px}

/* services */
.section-title{text-align:center}
.section-title h2{font-size:50px;color:var(--teal);font-weight:700;letter-spacing:1px}
.section-title .script{font-size:22px;color:var(--text);display:block;margin-top:2px}
.services{position:absolute;top:1020px;left:0;width:1200px;height:1048px}
.services .section-title{position:absolute;top:70px;width:100%}
.tabs{position:absolute;top:188px;left:150px;width:900px;display:flex;border-bottom:2px solid var(--line)}
.tabs div{flex:1;text-align:center;font-family:"Roboto Slab",serif;font-weight:700;font-size:17px;color:var(--ink);padding-bottom:12px;line-height:1.25}
.tabs div.on{color:var(--teal);border-bottom:4px solid var(--teal);margin-bottom:-3px}
.service-photo{position:absolute;top:300px;left:275px;width:650px;height:412px;background:linear-gradient(135deg,#6d5a4c 0%,#c9b9a8 45%,#e4e0da 70%,#7d6a5e 100%)}
.why{position:absolute;top:752px;width:100%;text-align:center}
.why h3{font-size:40px;color:var(--blue);font-weight:700}
.why p{width:680px;margin:14px auto 0;font-size:14px;line-height:1.75}
.why .btn{margin-top:34px;background:var(--teal)}

/* feature boxes */
.features{position:absolute;top:2068px;left:80px;width:1040px;height:356px;display:flex}
.feature{flex:1;color:var(--white);text-align:center;position:relative;padding-top:40px}
.feature.blue{background:var(--blue)}
.feature.teal{background:var(--teal)}
.feature .icon{width:96px;height:96px;border-radius:50%;border:3px solid var(--white);margin:0 auto;display:flex;align-items:center;justify-content:center}
.feature h4{font-family:"Roboto Slab",serif;font-size:20px;font-weight:700;margin-top:30px;text-transform:uppercase}
.feature ul{list-style:none;font-size:13px;line-height:1.9;margin-top:10px}
.feature .go{position:absolute;left:50%;bottom:14px;margin-left:-22px;width:44px;height:44px;border-radius:50%;background:var(--navy);display:flex;align-items:center;justify-content:center}

/* contact */
.contact{position:absolute;top:2424px;left:0;width:1200px;height:680px}
.contact .section-title{position:absolute;top:86px;width:100%}
.contact .section-title h2{color:var(--blue)}
.staff-photo{position:absolute;left:140px;top:216px;width:380px;height:386px;background:linear-gradient(160deg,#cfc6bd 0%,#e9e3dc 50%,#8a6f5e 100%)}
.employment{position:absolute;left:140px;top:572px;width:380px;height:58px;background:var(--blue);color:var(--white);font-family:"Roboto Slab",serif;font-weight:700;font-size:18px;display:flex;align-items:center;justify-content:center;text-transform:uppercase}
.contact-list{position:absolute;left:580px;top:230px;width:520px}
.contact-item{display:flex;gap:24px;margin-bottom:44px}
.contact-item .ico{flex:none;width:48px;height:48px;border-radius:50%;background:#e6f2f4;display:flex;align-items:center;justify-content:center}
.contact-item h5{font-family:"Roboto Slab",serif;font-size:17px;color:var(--teal);font-weight:700;text-transform:uppercase}
.contact-item p{font-size:13px;line-height:1.7;margin-top:6px}
.contact-item p b{color:var(--teal)}

/* cta */
.cta{position:absolute;top:3120px;left:0;width:1200px;height:300px;background:var(--teal);text-align:center;color:var(--white)}
.cta h3{font-family:"Roboto Slab",serif;font-size:34px;font-weight:700;width:860px;margin:76px auto 0;line-height:1.35}
.cta .btn{margin-top:30px;font-size:16px}

/* footer */
.site-footer{position:absolute;top:3420px;left:0;width:1200px;height:312px;background:var(--white)}
.footer-brand{position:absolute;left:110px;top:54px;width:150px;height:150px;border-radius:50%;border:3px solid var(--sky);display:flex;align-items:center;justify-content:center}
.footer-col{position:absolute;top:56px}
.footer-col h6{font-family:"Roboto Slab",serif;font-size:18px;color:var(--teal);font-weight:700;text-transform:uppercase;margin-bottom:12px}
.footer-col li{list-style:none;font-size:13px;line-height:2.1;display:flex;align-items:center;gap:8px}
.footer-col li::before{content:"";width:6px;height:6px;border-radius:50%;background:var(--teal)}
.copyright{position:absolute;left:0;bottom:0;width:100%;height:44px;border-top:1px solid var(--line);text-align:center;line-height:44px;font-size:12px}
</style>
</head>
<body>

<header class="site-header">
  <div class="brand">
    <div class="brand-dot"><span class="brand-name">Hearthside<br>Home</span></div>
  </div>
  <div class="header-phone">
    <div class="ico">
      <svg width="18" height="18" viewBox="0 0 24 24"><path fill="#fff" d="M6.6 10.8a15 15 0 006.6 6.6l2.2-2.2c.3-.3.7-.4 1-.2 1.1.4 2.3.6 3.6.6.6 0 1 .4 1 1V20c0 .6-.4 1-1 1A17 17 0 013 4c0-.6.4-1 1-1h3.5c.6 0 1 .4 1 1 0 1.3.2 2.5.6 3.6.1.3 0 .7-.2 1z"/></svg>
    </div>
    <div><small>Contact Us</small><strong>555-014-2290</strong></div>
  </div>
  <nav class="main-nav">
    <a class="active">&#9656; Home</a><a>About Us</a><a>Services</a><a>Contact Us</a>
  </nav>
</header>

<section class="hero">
  <div role="img" aria-label="Caregiver embracing an elderly woman seated in a wheelchair" style="position:absolute;inset:0"></div>
  <div class="hero-copy">
    <div class="kicker">Provide 24/7 Services</div>
    <h1>PROVIDING CARE</h1>
    <div class="sub">THROUGHOUT THE SOUTH SHORE</div>
    <span class="btn">Get Started</span>
  </div>
  <div class="hero-dots"><span></span><span></span><span></span><span class="on"></span></div>
</section>

<section class="about">
  <div class="about-badge">
    <h2 class="slab">ABOUT US</h2>
    <p class="script">Hearthside Home</p>
  </div>
  <div class="about-text">
    <p>Hearthside Home Health Services is owned and operated by Dana Whitfield, a registered nurse who has worked in the health care system since 2004. She has experienced home care, oncology, hospice and critical care. She holds a nursing license and has taught for nursing programs at local colleges and universities.</p>
    <p>At Hearthside Home caregivers have extensive background checks and training regarding HIPAA compliance. We understand the care of our clients in order to provide the best care possible in their home.</p>
    <span class="more">Read More &#9656;</span>
  </div>
</section>

<section class="services">
  <div class="section-title">
    <h2 class="slab">OUR SERVICES</h2>
    <span class="script">What We Do</span>
  </div>
  <div class="tabs">
    <div class="on">WHY CHOOSE<br>HOME CARE ?</div>
    <div>CARE SCHEDULE/<br>FREQUENCY</div>
    <div>PAYMENT<br>OPTIONS</div>
    <div>SERVICES<br>AREA MAP</div>
  </div>
  <div class="service-photo" role="img" aria-label="Nurse checking on an elderly man seated in his living room"></div>
  <div class="why">
    <h3 class="slab">WHY CHOOSE HOME CARE ?</h3>
    <p>Home care is a cost-effective option that allows clients the ability to receive necessary care in the comfort of their own home.</p>
    <p style="margin-top:6px">Home care can provide peace of mind to a family, and can help your loved one keep a sense of independence at home.</p>
    <span class="btn">Get Started</span>
  </div>
</section>

<div class="features">
  <div class="feature blue">
    <div class="icon"><svg width="48" height="48" viewBox="0 0 48 48" fill="none" stroke="#fff" stroke-width="2.5"><circle cx="24" cy="15" r="7"/><path d="M10 42c0-9 6-14 14-14s14 5 14 14"/><path d="M24 32v6M21 35h6"/></svg></div>
    <h4>Skilled Care Services</h4>
    <ul><li>Post Visit Nursing Assessment</li><li>Medication Management</li><li>Wound Care</li></ul>
    <div class="go"><svg width="16" height="16" viewBox="0 0 16 16"><path d="M6 3l5 5-5 5" stroke="#fff" stroke-width="2.5" fill="none"/></svg></div>
  </div>
  <div class="feature teal">
    <div class="icon"><svg width="50" height="50" viewBox="0 0 50 50" fill="none" stroke="#fff" stroke-width="2.5"><path d="M25 42S7 31 7 18a9 9 0 0118-3 9 9 0 0118 3c0 13-18 24-18 24z"/><path d="M10 25h9l3-6 4 11 3-5h11"/></svg></div>
    <h4>Non-Medical Services</h4>
    <ul><li>Live-In Care</li><li>Respite Care</li><li>Assisting with Daily Living Activities</li></ul>
    <div class="go"><svg width="16" height="16" viewBox="0 0 16 16"><path d="M6 3l5 5-5 5" stroke="#fff" stroke-width="2.5" fill="none"/></svg></div>
  </div>
  <div class="feature blue">
    <div class="icon"><svg width="52" height="48" viewBox="0 0 52 48" fill="none" stroke="#fff" stroke-width="2.5"><circle cx="18" cy="16" r="6"/><circle cx="35" cy="16" r="6"/><path d="M6 40c0-8 5-13 12-13s12 5 12 13"/><path d="M28 30c2-2 4-3 7-3 7 0 11 5 11 13"/></svg></div>
    <h4>Client Benefits</h4>
    <ul><li>Continuity of care with same</li><li>caregiver for each client to</li><li>ensure bonds</li></ul>
    <div class="go"><svg width="16" height="16" viewBox="0 0 16 16"><path d="M6 3l5 5-5 5" stroke="#fff" stroke-width="2.5" fill="none"/></svg></div>
  </div>
</div>

<section class="contact">
  <div class="section-title">
    <h2 class="slab">CONTACT US</h2>
    <span class="script">Keep In Touch</span>
  </div>
  <div class="staff-photo" role="img" aria-label="Portrait of the agency founder seated in a white coat"></div>
  <div class="employment">Employment Application</div>
  <div class="contact-list">
    <div class="contact-item">
      <div class="ico"><svg width="20" height="20" viewBox="0 0 20 20"><path d="M2 10l15-7-5 15-2-6z" fill="#2fb0ad"/></svg></div>
      <div><h5>Contact Online</h5><p>To contact us online, please fill out the care inquiry form below and you will be contacted within <b>24-48 hours</b>.</p></div>
    </div>
    <div class="contact-item">
      <div class="ico"><svg width="20" height="20" viewBox="0 0 24 24"><path fill="#2fb0ad" d="M6.6 10.8a15 15 0 006.6 6.6l2.2-2.2c.3-.3.7-.4 1-.2 1.1.4 2.3.6 3.6.6.6 0 1 .4 1 1V20c0 .6-.4 1-1 1A17 17 0 013 4c0-.6.4-1 1-1h3.5c.6 0 1 .4 1 1 0 1.3.2 2.5.6 3.6.1.3 0 .7-.2 1z"/></svg></div>
      <div><h5>Contact Buy Phone</h5><p>If you would like to speak with someone over the phone about your care inquiry, you can contact Hearthside Home <b>Monday-Friday 9:00am-5:00pm</b> at <b>555-014-2290</b>.</p></div>
    </div>
    <div class="contact-item">
      <div class="ico"><svg width="20" height="20" viewBox="0 0 20 20"><path d="M10 1a6 6 0 00-6 6c0 5 6 12 6 12s6-7 6-12a6 6 0 00-6-6zm0 8.5A2.5 2.5 0 1110 4.5a2.5 2.5 0 010 5z" fill="#2fb0ad"/></svg></div>
      <div><h5>Mailing Address</h5><p>Please mail all correspondence and employment applications to:<br><b>Hearthside Home Health Services</b><br><b>PO Box 417, Kestrel, MA 02999</b></p></div>
    </div>
  </div>
</section>

<section class="cta">
  <h3>If You Need An Have Any Question For Hearthside Home For Contact Us Today</h3>
  <span class="btn">Care Inquiry Form</span>
</section>

<footer class="site-footer">
  <div class="footer-brand"><span class="brand-name">Hearthside<br>Home</span></div>
  <div class="footer-col" style="left:430px"><h6>Sitemap</h6><ul><li>Home</li><li>About Us</li><li>Services</li><li>Contact Us</li></ul></div>
  <div class="footer-col" style="left:680px"><h6>Contact Us</h6><ul><li>555-014-2290</li><li>PO Box 417</li><li>Kestrel, MA 02999</li></ul></div>
  <div class="footer-col" style="left:940px"><h6>Quick Links</h6><ul><li>Privacy Policy</li><li>Terms &amp; Condition</li><li>Newsletter</li><li>Payment</li></ul></div>
  <div class="copyright">&copy; Hearthside Home Health Services. All Rights Reserved.</div>
</footer>

</body>
</html>
```